Website for IT consulting Company

I need a website upgrade, the existing site content is ok, I would also like to add a testimonial page, the site should be something that is easy for us to update content. You use the content from www.velmarketa.com as an example. I will also post update logo and artwork. I also need a contact form with some type of validation or captcha.

Please omit Address maps

Target Market(s)

small business, service oriented companies. We provide IT Consulting, support and mangement

Industry/Entity Type

Information Technology

Coding

Coded - Design and coding required

Number of Pages Required

1 page

Font styles to use
Serif
Sans Serif

Requirements
Must have
• Contain logo attached, and content from existing web site www.velmarketa.com.
• Also need to update content easily, and be movable to different platforms.
• There is a catch phrase
• "Let us worry about your technology…” “ so you don’t have to!”
• Should be included.
Nice to have
• Testimonial page, Project page where we can post new and past projects and pictures
Should not have
• none

```html
<!DOCTYPE html>
<html lang="en">
<head>
<meta charset="utf-8">
<title>Velmarketa – IT Consulting</title>
<link rel="stylesheet" href="https://fonts.googleapis.com/css2?family=Exo+2:wght@600;700;800&family=Lato:ital,wght@0,400;0,700;0,900;1,400&display=swap">
<style>
:root{
  --orange:#f07f1e;
  --orange-dark:#d96a10;
  --ink:#1d1d1d;
  --text:#333;
  --muted:#777;
  --line:#d6d6d6;
  --light:#f1f1f1;
  --white:#fff;
  --footer:#1f1f1f;
  --footer-bar:#111;
  --hero-dark:#3a3a3a;
  --hero-mid:#6a6a6a;
}
*{box-sizing:border-box;margin:0;padding:0}
html,body{width:1200px;height:2752px;overflow:hidden}
body{font-family:"Lato",Arial,sans-serif;color:var(--text);background:var(--white);position:relative}
.heading{font-family:"Exo 2",Arial,sans-serif;font-weight:800;color:var(--ink);text-transform:uppercase}
.heading em{font-style:normal;color:var(--orange)}
.abs{position:absolute}

/* top bar */
.topbar{position:absolute;top:0;left:0;width:1200px;height:33px;background:var(--orange);color:var(--white);font-size:14px;font-weight:700}
.topbar .contact{position:absolute;left:85px;top:8px;display:flex;gap:26px;align-items:center}
.topbar .contact span{display:flex;align-items:center;gap:7px}
.social{display:flex;gap:8px}
.social i{display:block;width:24px;height:24px;border-radius:50%;background:#1d6fc4;border:2px solid var(--white)}
.topbar .social{position:absolute;right:90px;top:4px}

/* header */
.header{position:absolute;top:33px;left:0;width:1200px;height:99px;background:var(--white)}
.brand{position:absolute;left:85px;top:22px;display:flex;align-items:center;gap:10px}
.brand .mark{width:40px;height:40px;background:var(--orange)}
.brand .name{font-family:"Exo 2",Arial,sans-serif;font-weight:800;font-size:36px;color:#6c6c6c;letter-spacing:1px}
.brand-tag{position:absolute;left:137px;top:72px;font-size:9px;color:var(--orange)}
.nav{position:absolute;right:86px;top:62px;display:flex;gap:33px;font-family:"Exo 2",Arial,sans-serif;font-weight:700;font-size:13.5px;color:var(--ink)}
.nav .active{color:var(--orange);border-bottom:2px solid var(--orange);padding-bottom:3px}

/* hero */
.hero{position:absolute;top:132px;left:0;width:1200px;height:473px;background:linear-gradient(90deg,#2b2b2b 0%,var(--hero-mid) 60%,var(--hero-dark) 100%)}
.hero-art{position:absolute;left:0;top:0;width:600px;height:473px;background:radial-gradient(circle at 45% 55%,#4aa3d9 0%,#1f5f8f 35%,#243040 70%,transparent 100%)}
.hero-copy{position:absolute;left:690px;top:170px;width:420px;text-align:center;color:var(--white)}
.hero-copy h1{font-family:"Exo 2",Arial,sans-serif;font-weight:700;font-size:28px;line-height:32px}
.hero-copy p{margin-top:14px;font-weight:700;font-size:15px;line-height:21px}
.btn{display:inline-block;background:var(--orange);color:var(--white);font-family:"Exo 2",Arial,sans-serif;font-weight:700;font-size:13px;padding:8px 22px;border-radius:3px;text-transform:uppercase}
.hero-copy .btn{margin-top:20px}
.dots{position:absolute;left:563px;top:430px;display:flex;gap:7px}
.dots i{width:11px;height:11px;border-radius:50%;border:2px solid var(--white)}
.dots i.on{background:var(--orange)}
.side-tabs{position:absolute;right:0;top:275px;display:flex;flex-direction:column;gap:2px}
.side-tabs i{display:block;width:30px;height:28px;background:#3c5a99}
.side-tabs i:nth-child(2){background:#a0785a}
.side-tabs i:nth-child(3){background:#1da1f2}
.side-tabs i:nth-child(4){background:#d63a2c}

/* about */
.about{position:absolute;top:605px;left:0;width:1200px;height:302px;text-align:center}
.about .heading{position:absolute;top:50px;width:100%;font-size:33px;display:flex;justify-content:center;align-items:center;gap:14px}
.about .heading .mark{width:32px;height:32px;background:var(--orange)}
.about p{position:absolute;left:168px;top:120px;width:864px;font-size:13.5px;line-height:23px;color:var(--ink)}
.about .btn-grey{position:absolute;left:533px;top:215px;background:linear-gradient(#8d8d8d,#5f5f5f);color:var(--white);font-family:"Exo 2",Arial,sans-serif;font-weight:700;font-size:13px;padding:8px 20px;border-radius:3px}

/* services */
.services{position:absolute;top:907px;left:0;width:1200px;height:453px;background:var(--light)}
.section-title{position:absolute;width:100%;text-align:center;font-size:31px}
.rule{position:absolute;left:363px;width:474px;height:1px;background:#bdbdbd}
.rule::after{content:"";position:absolute;left:217px;top:-1px;width:40px;height:3px;background:var(--orange)}
.services .section-title{top:46px}
.services .rule{top:101px}
.card{position:absolute;top:148px;width:280px;height:260px;background:var(--white);box-shadow:0 1px 3px rgba(0,0,0,.15)}
.card .photo{height:205px}
.card .label{position:absolute;left:12px;top:213px;font-family:"Exo 2",Arial,sans-serif;font-weight:700;font-size:15px;line-height:18px;color:var(--ink);text-transform:uppercase}
.card .go{position:absolute;right:0;top:205px;width:55px;height:55px;background:var(--orange);display:flex;align-items:center;justify-content:center}

/* support grid */
.support{position:absolute;top:1360px;left:0;width:1200px;height:500px}
.support .section-title{top:50px}
.support .rule{top:110px}
.tile{position:absolute}
.tile .cap{position:absolute;left:0;bottom:0;width:100%;height:30px;background:rgba(0,0,0,.75);color:var(--white);font-family:"Exo 2",Arial,sans-serif;font-weight:600;font-size:12.5px;display:flex;align-items:center;justify-content:center;text-transform:uppercase}

/* outsourcing + testimonials */
.info{position:absolute;top:1860px;left:0;width:1200px;height:365px;background:var(--light)}
.col-title{position:absolute;top:42px;font-size:23px}
.col-rule{position:absolute;top:88px;height:1px;background:#bbb}
.outsourcing{position:absolute;left:161px;top:112px;width:410px;font-size:12.5px;line-height:19.5px;color:var(--ink)}
.ticks{list-style:none;margin-top:4px}
.ticks li{position:relative;padding-left:26px;margin-top:2px}
.ticks svg{position:absolute;left:0;top:3px}
.divider{position:absolute;left:600px;top:40px;width:1px;height:280px;background:#d0d0d0}
.pager{position:absolute;top:44px;display:flex;gap:4px}
.pager span{width:24px;height:24px;border:1px solid #bbb;display:flex;align-items:center;justify-content:center;background:var(--white)}
.pager span.on{border-color:var(--orange)}
.avatar{position:absolute;left:628px;top:115px;width:82px;height:82px;border-radius:50%;border:4px solid var(--orange);background:radial-gradient(circle,#9ab4c8,#486a86)}
.quote{position:absolute;left:730px;top:112px;width:300px;font-style:italic;font-size:12.5px;line-height:21px;color:#666}
.quote .q{font-family:Georgia,serif;font-size:28px;color:#bbb;font-style:normal;line-height:10px;vertical-align:-8px}
.author{position:absolute;left:730px;top:285px;font-family:"Exo 2",Arial,sans-serif;font-weight:800;font-size:13px;color:var(--ink)}

/* clients */
.clients{position:absolute;top:2225px;left:0;width:1200px;height:230px}
.clients .section-title{top:36px}
.clients .rule{top:85px}
.client{position:absolute;top:120px;width:128px;height:68px;border:1px solid #cfcfcf;display:flex;align-items:center;justify-content:center;font-family:"Lato",Arial,sans-serif;font-weight:900;font-size:15px;color:#222;letter-spacing:1px;text-transform:uppercase}
.chev{position:absolute;top:137px}

/* footer */
.footer{position:absolute;top:2455px;left:0;width:1200px;height:257px;background:var(--footer);color:#cfcfcf}
.foot-title{position:absolute;top:40px;font-family:"Exo 2",Arial,sans-serif;font-weight:700;font-size:16px;color:var(--white)}
.foot-rule{position:absolute;top:65px;height:1px;background:#555}
.links{position:absolute;left:161px;top:82px;list-style:none;font-size:11px;line-height:22px}
.links li::before{content:"•";margin-right:7px}
.contact-list{position:absolute;left:316px;top:80px;font-size:11.5px;width:210px}
.contact-list b{display:block;font-family:"Exo 2",Arial,sans-serif;color:var(--white);font-size:13px}
.contact-list .row{display:flex;align-items:center;gap:12px;margin-top:20px}
.form{position:absolute;left:568px;top:80px;width:227px}
.field{height:30px;border:1px solid #666;margin-bottom:8px;font-size:11px;padding:8px 10px;color:#ddd}
.field.msg{height:36px}
.form .btn{font-size:13px;padding:7px 16px;border-radius:0}
.foot-brand{position:absolute;left:845px;top:95px;display:flex;align-items:center;gap:10px}
.foot-brand .mark{width:36px;height:36px;background:#444}
.foot-brand .name{font-family:"Exo 2",Arial,sans-serif;font-weight:800;font-size:30px;color:#8a8a8a}
.bottombar{position:absolute;top:2712px;left:0;width:1200px;height:40px;background:var(--footer-bar);color:#ccc;font-size:11px}
.bottombar .copy{position:absolute;left:161px;top:14px}
.bottombar .social{position:absolute;right:160px;top:8px}
</style>
</head>
<body>

<div class="topbar">
  <div class="contact">
    <span><svg width="13" height="13" viewBox="0 0 24 24"><path fill="#fff" d="M6.6 10.8a15 15 0 0 0 6.6 6.6l2.2-2.2c.3-.3.7-.4 1-.2 1.1.4 2.3.6 3.6.6.6 0 1 .4 1 1V20c0 .6-.4 1-1 1A17 17 0 0 1 3 4c0-.6.4-1 1-1h3.5c.6 0 1 .4 1 1 0 1.3.2 2.5.6 3.6.1.3 0 .7-.2 1z"/></svg>123-456-7890</span>
    <span>|</span>
    <span><svg width="14" height="11" viewBox="0 0 24 18"><rect x="1" y="1" width="22" height="16" fill="none" stroke="#fff" stroke-width="2"/><path d="M1 1l11 9 11-9" fill="none" stroke="#fff" stroke-width="2"/></svg>mail@velmarketa.com</span>
  </div>
  <div class="social"><i></i><i></i><i></i></div>
</div>

<header class="header">
  <div class="brand"><span class="mark"></span><span class="name">VELMARKETA</span></div>
  <div class="brand-tag">Let us worry about your technology... So you don't have to!</div>
  <nav class="nav">
    <span class="active">HOME</span><span>ABOUT US</span><span>SERVICES</span><span>PROJECTS</span><span>CAREER</span><span>TESTIMONIALS</span><span>CONTACT US</span>
  </nav>
</header>

<section class="hero">
  <div class="hero-art" role="img" aria-label="Businessman holding a glowing globe surrounded by connected devices and app icons"></div>
  <div class="hero-copy">
    <h1>Let Us Worry About<br>Your Technology…<br>So You Don't Have To!</h1>
    <p>Our Mission Is Helping Businesses &amp; Individuals Realize A Return On Investment By Implementing Today's Advanced Technologies.</p>
    <span class="btn">Get Started</span>
  </div>
  <div class="dots"><i class="on"></i><i></i><i></i><i></i></div>
</section>
<div class="side-tabs"><i></i><i></i><i></i><i></i></div>

<section class="about">
  <h2 class="heading">About <span class="mark"></span> Velmarketa Development Group, Inc</h2>
  <p>Our clients choose Velmarketa and stay with us because we deliver on every technology need they have. We have a 90% client retention rate. Many of our clients span ten or more years. Whether you need to completely outsource your IT requirements or add advanced insight to your existing IT department, Velmarketa can serve as your complete outsourcing or as a compliment to your IT staff.</p>
  <span class="btn-grey">READ MORE</span>
</section>

<section class="services">
  <h2 class="heading section-title">Our <em>Services</em></h2>
  <div class="rule"></div>
  <div class="card" style="left:161px">
    <div class="photo" role="img" aria-label="Business team reviewing documents at a desk" style="background:linear-gradient(135deg,#e8eef3,#2c3e55)"></div>
    <div class="label">Managed<br>IT Solutions</div>
    <div class="go"><svg width="22" height="18" viewBox="0 0 22 18"><path d="M1 9h16M11 2l8 7-8 7" fill="none" stroke="#fff" stroke-width="3"/></svg></div>
  </div>
  <div class="card" style="left:461px">
    <div class="photo" role="img" aria-label="Support staff with headsets working at monitors" style="background:linear-gradient(135deg,#dfe8ef,#7f9bb3)"></div>
    <div class="label">Remote Diagnostics<br>&amp; Support</div>
    <div class="go"><svg width="22" height="18" viewBox="0 0 22 18"><path d="M1 9h16M11 2l8 7-8 7" fill="none" stroke="#fff" stroke-width="3"/></svg></div>
  </div>
  <div class="card" style="left:761px">
    <div class="photo" role="img" aria-label="Hand on a computer mouse in front of data charts" style="background:linear-gradient(135deg,#4f8fa8,#cfe3ea)"></div>
    <div class="label">IT Infrastructure<br>&amp; Design</div>
    <div class="go"><svg width="22" height="18" viewBox="0 0 22 18"><path d="M1 9h16M11 2l8 7-8 7" fill="none" stroke="#fff" stroke-width="3"/></svg></div>
  </div>
</section>

<section class="support">
  <h2 class="heading section-title">IT Support <em>Solutions</em></h2>
  <div class="rule"></div>
  <div class="tile" style="left:161px;top:153px;width:317px;height:272px;background:linear-gradient(160deg,#8fa5b8,#3f5264)" role="img" aria-label="Technician working on a laptop in a server room"><div class="cap">Network Administration</div></div>
  <div class="tile" style="left:486px;top:153px;width:330px;height:127px;background:linear-gradient(135deg,#f2f2f2,#9a9a9a)" role="img" aria-label="Man working at a desktop computer"><div class="cap">Desktop Support</div></div>
  <div class="tile" style="left:486px;top:288px;width:162px;height:137px;background:linear-gradient(135deg,#2a4f7a,#6a8fb4)" role="img" aria-label="Technician connecting network cables in a rack"><div class="cap">Network Cabling</div></div>
  <div class="tile" style="left:656px;top:288px;width:160px;height:137px;background:linear-gradient(180deg,#c4d4e4,#5f7893)" role="img" aria-label="Person with a phone in front of a city skyline"><div class="cap">Wireless Networks</div></div>
  <div class="tile" style="left:824px;top:153px;width:216px;height:272px;background:linear-gradient(160deg,#d7dbe6,#8b93b5 60%,#b36b86)" role="img" aria-label="Businessman touching a shield security symbol"><div class="cap">Antivirus Solutions</div></div>
</section>

<section class="info">
  <h3 class="heading col-title" style="left:161px">Outsourcing <em>Technology</em></h3>
  <div class="col-rule" style="left:161px;width:410px"></div>
  <div class="outsourcing">
    <p>Outsourcing is subcontracting a process, such as product design or manufacturing, to a third-party company. [1] The decision to outsource is often made in the interest of lowering firm costs, redirecting or conserving energy directed at the competencies of a particular business, or to make more efficient use of land, labor, capital, (information) technology and resources.</p>
    <ul class="ticks">
      <li><svg width="15" height="14" viewBox="0 0 15 14"><rect x="0.5" y="2.5" width="11" height="11" fill="none" stroke="#222"/><path d="M3 7l3 3 8-9" fill="none" stroke="#222" stroke-width="2"/></svg>Outsourcing became part of the business lexicon during the 1980s.</li>
      <li><svg width="15" height="14" viewBox="0 0 15 14"><rect x="0.5" y="2.5" width="11" height="11" fill="none" stroke="#222"/><path d="M3 7l3 3 8-9" fill="none" stroke="#222" stroke-width="2"/></svg>In today's world, companies are expected to use technology to function and stay competitive.</li>
      <li><svg width="15" height="14" viewBox="0 0 15 14"><rect x="0.5" y="2.5" width="11" height="11" fill="none" stroke="#222"/><path d="M3 7l3 3 8-9" fill="none" stroke="#222" stroke-width="2"/></svg>However, this aspect of business provides many challenges that most companies cannot solve on their own.</li>
    </ul>
  </div>
  <div class="divider"></div>
  <h3 class="heading col-title" style="left:634px">Clients <em>Testimonials</em></h3>
  <div class="col-rule" style="left:634px;width:406px"></div>
  <div class="pager" style="left:984px">
    <span><svg width="8" height="12" viewBox="0 0 8 12"><path d="M7 1L2 6l5 5" fill="none" stroke="#999" stroke-width="1.5"/></svg></span>
    <span class="on"><svg width="8" height="12" viewBox="0 0 8 12"><path d="M1 1l5 5-5 5" fill="none" stroke="#f07f1e" stroke-width="1.5"/></svg></span>
  </div>
  <div class="avatar" role="img" aria-label="Portrait of the client"></div>
  <p class="quote"><span class="q">“</span> Duis autem vel eum iriure dolor in hendrerit in vulputate velit esse molestie consequat, velm mol illumkj dolore eu feugiat nulla facilisis at vero eron etmoln accumsan et iusto odio dignissim quiosmik blandit morm vulputate velit esse molestie consel quat, vel illumklj dolore facilisis. <span class="q">”</span></p>
  <div class="author">- MR. DORIAN VELL</div>
</section>

<section class="clients">
  <h2 class="heading section-title">Our <em>Clients</em></h2>
  <div class="rule"></div>
  <svg class="chev" style="left:123px" width="18" height="36" viewBox="0 0 18 36"><path d="M16 2L3 18l13 16" fill="none" stroke="#bbb" stroke-width="2"/></svg>
  <div class="client" style="left:161px">Halden</div>
  <div class="client" style="left:311px">Norvik</div>
  <div class="client" style="left:461px">Tessel</div>
  <div class="client" style="left:611px">Marrow</div>
  <div class="client" style="left:762px">Quillon</div>
  <div class="client" style="left:912px">Brisca</div>
  <svg class="chev" style="left:1058px" width="18" height="36" viewBox="0 0 18 36"><path d="M2 2l13 16L2 34" fill="none" stroke="#bbb" stroke-width="2"/></svg>
</section>

<footer class="footer">
  <div class="foot-title" style="left:161px">QUICK LINKS</div>
  <div class="foot-rule" style="left:161px;width:115px"></div>
  <ul class="links"><li>Home</li><li>About Us</li><li>Services</li><li>Projects</li><li>Career</li><li>Testimonials</li><li>Contact Us</li></ul>

  <div class="foot-title" style="left:316px">CONTACT DETAILS</div>
  <div class="foot-rule" style="left:316px;width:210px"></div>
  <div class="contact-list">
    <b>VELMARKETA</b>4821 Harbor Lane, Cedar Point.
    <div class="row"><svg width="12" height="12" viewBox="0 0 24 24"><path fill="#ccc" d="M6.6 10.8a15 15 0 0 0 6.6 6.6l2.2-2.2c.3-.3.7-.4 1-.2 1.1.4 2.3.6 3.6.6.6 0 1 .4 1 1V20c0 .6-.4 1-1 1A17 17 0 0 1 3 4c0-.6.4-1 1-1h3.5c.6 0 1 .4 1 1 0 1.3.2 2.5.6 3.6.1.3 0 .7-.2 1z"/></svg>123-456-7890</div>
    <div class="row"><svg width="12" height="12" viewBox="0 0 24 24"><rect x="6" y="2" width="12" height="6" fill="#ccc"/><rect x="2" y="9" width="20" height="9" fill="#ccc"/><rect x="6" y="15" width="12" height="7" fill="#ccc" stroke="#1f1f1f" stroke-width="2"/></svg>123-456-7890</div>
    <div class="row"><svg width="12" height="10" viewBox="0 0 24 18"><rect x="1" y="1" width="22" height="16" fill="#ccc"/><path d="M1 1l11 9 11-9" fill="none" stroke="#1f1f1f" stroke-width="2"/></svg>mail@velmarketa.com</div>
  </div>

  <div class="foot-title" style="left:568px">QUICK INQUIRY</div>
  <div class="form">
    <div class="field">Name</div>
    <div class="field">Email</div>
    <div class="field msg">Message</div>
    <span class="btn">SUBMIT</span>
  </div>

  <div class="foot-brand"><span class="mark"></span><span class="name">VELMARKETA</span></div>
</footer>

<div class="bottombar">
  <div class="copy">COPYRIGHT © 2017 VELMARKETA.COM. ALL RIGHT RESERVED.</div>
  <div class="social"><i></i><i></i><i></i></div>
</div>

</body>
</html>
```